Harrowgate - Pell Corporate PowerPoint Presentation Template

A custom, corporate template that is highly professional, neat/crisp, "serious," and captures/emphasizes the essence of a global, mutli-brand consumer products company that has deep tradition and values family, hard work, performance, innovation, and service to our consumers and retail partners.
The company's roots and headquarters are in Texas. We are a private and family owned since our founding almost 100 years ago. The corporate website is www.hpvcorp-example.com and other branded websites can be accessed from this site.
Our current presentation title page is attached. We believe it to be somewhat stale/out of date and less sophisticated that the image we'd prefer to project. We occasionally add/change logos and will have to adapt the presentation. These presentations must look good printed.
Please contact me with any questions or requests and I will respond very quickly.
Target Market(s)
Corporate Executives
Industry/Entity Type
It Professional
Requirements
Must have
- Sans Serif font (can't select below). Industry is Apparel and Footwear / Consumer Products (can't select below).

```html
<!DOCTYPE html>
<html lang="en">
<head>
<meta charset="utf-8">
<title>Harrowgate - Pell Presentation Template</title>
<link rel="stylesheet" href="https://fonts.googleapis.com/css2?family=Carlito:wght@400;700&display=swap">
<style>
  :root {
    --stage: #686767;
    --paper: #ffffff;
    --header-bg: #f5f5f5;
    --header-rule: #dcdcdc;
    --brand-blue: #0a4fa0;
    --title-blue: #1a5aa8;
    --stripe: #dae4f0;
    --muted: #a8a8a8;
    --body-text: #8a8a8a;
    --dash: #9a9a9a;
    --bar-yellow: #ffff00;
    --bar-gray: #bfbfbf;
    --bar-blue: #0a56a8;
    --bar-red: #d9143c;
    --line-red: #c00000;
    --marker-orange: #ed7d31;
    --line-gray: #a5a5a5;
  }
  * { box-sizing: border-box; margin: 0; padding: 0; }
  html, body { width: 1200px; height: 926px; overflow: hidden; background: var(--stage); }
  body { position: relative; font-family: "Carlito", "Calibri", sans-serif; }

  .slide { position: absolute; background: var(--paper); overflow: hidden; }
  .slide--section { left: 37px; top: 26px; width: 552px; height: 414px; }
  .slide--table { left: 606px; top: 26px; width: 549px; height: 412px; }
  .slide--bars { left: 38px; top: 474px; width: 546px; height: 410px; }
  .slide--lines { left: 607px; top: 474px; width: 550px; height: 410px; }

  /* Section slide */
  .section-photo { position: absolute; inset: 0;
    background: radial-gradient(circle at 70% 65%, #5a6fa0 0%, #2f5590 35%, #1d3f7a 70%, #15356a 100%); }
  .section-badge { position: absolute; left: 189px; top: 130px; width: 172px; height: 172px;
    border-radius: 50%; border: 3px solid #fff; background: rgba(170, 190, 215, 0.55);
    display: flex; align-items: center; justify-content: center; }
  .section-badge__name { color: #fff; font-weight: 700; font-size: 17px; }
  .section-title { position: absolute; left: 385px; top: 352px; color: #fff; font-size: 20px; }

  /* Header */
  .slide-header { position: absolute; left: 0; top: 0; right: 0; height: 62px;
    background: var(--header-bg); border-bottom: 2px solid var(--header-rule); }
  .brand-name { position: absolute; left: 46px; top: 24px; color: var(--brand-blue);
    font-weight: 700; font-size: 12px; }
  .slide-heading { position: absolute; right: 50px; top: 14px; text-align: center; }
  .slide-heading__title { color: var(--title-blue); font-size: 20px; line-height: 22px; }
  .slide-heading__sub { color: #666; font-size: 8px; }

  /* Table */
  .data-table { position: absolute; left: 41px; top: 121px; width: 466px; border-collapse: collapse;
    table-layout: fixed; }
  .data-table th { background: var(--brand-blue); color: #fff; font-weight: 400; font-size: 11px;
    height: 29px; border-right: 1px solid #fff; }
  .data-table td { color: var(--muted); font-size: 9px; text-align: center; height: 30px;
    border-right: 1px solid #f0f0f0; }
  .data-table tr.is-striped td { background: var(--stripe); }

  .body-copy { position: absolute; left: 40px; width: 460px; color: var(--body-text);
    font-size: 6.5px; line-height: 9px; }
  .slide--bars .body-copy, .slide--lines .body-copy { line-height: 13.6px; width: 470px; }
  .body-copy em { font-style: italic; font-weight: 700; color: #666; }

  /* Footer */
  .slide-footer { position: absolute; left: 0; right: 0; height: 10px; }
  .slide-footer__rule { position: absolute; left: 0; width: 488px; top: 0; height: 8px;
    border-top: 2px dashed var(--dash); border-bottom: 2px dashed var(--dash); }
  .slide-footer__num { position: absolute; left: 502px; top: 0; font-size: 7px; font-weight: 700; color: #444; }
  .slide-footer__tail { position: absolute; left: 522px; right: 0; top: 0; height: 8px;
    border-top: 2px dashed var(--dash); border-bottom: 2px dashed var(--dash); }

  .chart { position: absolute; left: 0; top: 0; }
  .chart text { font-family: "Carlito", "Calibri", sans-serif; }
</style>
</head>
<body>

<!-- Section slide -->
<section class="slide slide--section">
  <div class="section-photo" role="img" aria-label="Blue-tinted photo of a worker in workwear and gloves handling a tool"></div>
  <div class="section-badge"><span class="section-badge__name">Harrowgate - Pell</span></div>
  <p class="section-title">Section Title</p>
</section>

<!-- Table slide -->
<section class="slide slide--table">
  <header class="slide-header">
    <span class="brand-name">Harrowgate - Pell</span>
    <div class="slide-heading">
      <h2 class="slide-heading__title" style="font-weight:400">Table Slide</h2>
      <p class="slide-heading__sub">Lorem ipsum dolor sit amet consectetur</p>
    </div>
  </header>
  <table class="data-table">
    <thead><tr><th>Lorem ipsum</th><th>Lorem ipsum</th><th>Lorem ipsum</th><th>Lorem ipsum</th></tr></thead>
    <tbody>
      <tr><td>sample text</td><td>sample text</td><td>sample text</td><td>sample text</td></tr>
      <tr class="is-striped"><td>sample text</td><td>sample text</td><td>sample text</td><td>sample text</td></tr>
      <tr><td>sample text</td><td>sample text</td><td>sample text</td><td>sample text</td></tr>
      <tr class="is-striped"><td>sample text</td><td>sample text</td><td>sample text</td><td>Lorem ipsum</td></tr>
      <tr><td>sample text</td><td>sample text</td><td>sample text</td><td>Lorem ipsum</td></tr>
    </tbody>
  </table>
  <p class="body-copy" style="top:324px">Lorem ipsum dolor sit amet, <em>consectetur adipiscing elit.</em> Praesent sodales odio sit amet odio tristique quis tempus odio Lorem ipsum dolor sit amet, consectetur adipiscing elit. Lorem ipsum dolor sit amet, consectetur adipiscing elit. Praesent sodales odio sit amet odio tristique quis tempus odio Lorem ipsum dolor sit amet, consectetur adipiscing elit.</p>
  <footer class="slide-footer" style="top:390px">
    <div class="slide-footer__rule"></div><span class="slide-footer__num">8</span><div class="slide-footer__tail"></div>
  </footer>
</section>

<!-- Bar chart slide -->
<section class="slide slide--bars">
  <header class="slide-header">
    <span class="brand-name">Harrowgate - Pell</span>
    <div class="slide-heading">
      <h2 class="slide-heading__title" style="font-weight:400">Chart Slide</h2>
      <p class="slide-heading__sub">Lorem ipsum dolor sit amet consectetur</p>
    </div>
  </header>
  <svg class="chart" width="546" height="410" viewBox="0 0 546 410">
    <g stroke="#f0f0f0" stroke-width="0.6">
      <line x1="48" x2="470" y1="120" y2="120"/><line x1="48" x2="470" y1="142.4" y2="142.4"/>
      <line x1="48" x2="470" y1="164.9" y2="164.9"/><line x1="48" x2="470" y1="187.3" y2="187.3"/>
      <line x1="48" x2="470" y1="209.7" y2="209.7"/><line x1="48" x2="470" y1="232.1" y2="232.1"/>
      <line x1="48" x2="470" y1="254.6" y2="254.6"/>
    </g>
    <line x1="48" y1="120" x2="48" y2="277" stroke="#999" stroke-width="0.6"/>
    <line x1="48" y1="277" x2="470" y2="277" stroke="#999" stroke-width="0.6"/>
    <g font-size="5" fill="#777" text-anchor="end">
      <text x="44" y="122">70</text><text x="44" y="144">60</text><text x="44" y="167">50</text>
      <text x="44" y="189">40</text><text x="44" y="211">30</text><text x="44" y="234">20</text>
      <text x="44" y="256">10</text><text x="44" y="279">0</text>
    </g>
    <g>
      <rect x="60.2" y="205.2" width="15" height="71.8" fill="var(--bar-yellow)"/>
      <rect x="75.2" y="220.9" width="15" height="56.1" fill="var(--bar-gray)"/>
      <rect x="90.2" y="243.4" width="15" height="33.6" fill="var(--bar-blue)"/>
      <rect x="105.2" y="250.1" width="15" height="26.9" fill="var(--bar-red)"/>

      <rect x="144.6" y="205.2" width="15" height="71.8" fill="var(--bar-yellow)"/>
      <rect x="159.6" y="198.5" width="15" height="78.5" fill="var(--bar-gray)"/>
      <rect x="174.6" y="225.4" width="15" height="51.6" fill="var(--bar-blue)"/>
      <rect x="189.6" y="250.1" width="15" height="26.9" fill="var(--bar-red)"/>

      <rect x="229" y="214.2" width="15" height="62.8" fill="var(--bar-yellow)"/>
      <rect x="244" y="232.1" width="15" height="44.9" fill="var(--bar-gray)"/>
      <rect x="259" y="142.4" width="15" height="134.6" fill="var(--bar-blue)"/>
      <rect x="274" y="250.1" width="15" height="26.9" fill="var(--bar-red)"/>

      <rect x="313.4" y="250.1" width="15" height="26.9" fill="var(--bar-yellow)"/>
      <rect x="328.4" y="209.7" width="15" height="67.3" fill="var(--bar-gray)"/>
      <rect x="343.4" y="169.3" width="15" height="107.7" fill="var(--bar-blue)"/>
      <rect x="358.4" y="229.9" width="15" height="47.1" fill="var(--bar-red)"/>

      <rect x="397.8" y="243.4" width="15" height="33.6" fill="var(--bar-yellow)"/>
      <rect x="412.8" y="218.7" width="15" height="58.3" fill="var(--bar-gray)"/>
      <rect x="427.8" y="160.4" width="15" height="116.6" fill="var(--bar-blue)"/>
      <rect x="442.8" y="214.2" width="15" height="62.8" fill="var(--bar-red)"/>
    </g>
    <g font-size="5" fill="#777" text-anchor="middle">
      <text x="90.2" y="286">5/1/2015</text><text x="174.6" y="286">6/1/2015</text>
      <text x="259" y="286">7/1/2015</text><text x="343.4" y="286">8/1/2015</text>
      <text x="427.8" y="286">9/1/2015</text>
    </g>
    <g font-size="5" fill="#777">
      <rect x="481" y="183" width="8" height="6" fill="var(--bar-blue)"/><text x="496" y="188">Indonesia</text>
      <rect x="481" y="201" width="8" height="6" fill="var(--bar-yellow)"/><text x="496" y="206">Indonesia</text>
      <rect x="481" y="219" width="8" height="6" fill="var(--bar-red)"/><text x="496" y="224">Indonesia</text>
      <rect x="481" y="240" width="8" height="6" fill="var(--bar-gray)"/><text x="496" y="245">Indonesia</text>
    </g>
  </svg>
  <p class="body-copy" style="top:316px">Lorem ipsum dolor sit amet, <em>consectetur adipiscing elit.</em> Praesent sodales odio sit amet odio tristique quis tempus odio Lorem ipsum dolor sit amet, consectetur adipiscing elit. Lorem ipsum dolor sit amet, consectetur adipiscing elit. Praesent sodales odio sit amet odio tristique quis tempus odio Lorem ipsum dolor sit amet, consectetur adipiscing elit. Lorem ipsum dolor sit amet, consectetur adipiscing elit.</p>
  <footer class="slide-footer" style="top:388px">
    <div class="slide-footer__rule"></div><span class="slide-footer__num">5</span><div class="slide-footer__tail"></div>
  </footer>
</section>

<!-- Line chart slide -->
<section class="slide slide--lines">
  <header class="slide-header">
    <span class="brand-name">Harrowgate - Pell</span>
    <div class="slide-heading">
      <h2 class="slide-heading__title" style="font-weight:400">Chart Slide</h2>
      <p class="slide-heading__sub">Lorem ipsum dolor sit amet consectetur</p>
    </div>
  </header>
  <svg class="chart" width="550" height="410" viewBox="0 0 550 410">
    <g stroke="#bdbdbd" stroke-width="0.8">
      <line x1="63" x2="437" y1="99" y2="99"/><line x1="63" x2="437" y1="128.8" y2="128.8"/>
      <line x1="63" x2="437" y1="158.6" y2="158.6"/><line x1="63" x2="437" y1="188.4" y2="188.4"/>
      <line x1="63" x2="437" y1="218.2" y2="218.2"/><line x1="63" x2="437" y1="248" y2="248"/>
      <line x1="63" x2="437" y1="278" y2="278"/>
      <line x1="63" x2="63" y1="99" y2="278"/>
    </g>
    <g font-size="9" fill="#555" text-anchor="end">
      <text x="56" y="102">6</text><text x="56" y="132">5</text><text x="56" y="162">4</text>
      <text x="56" y="192">3</text><text x="56" y="221">2</text><text x="56" y="251">1</text>
      <text x="56" y="281">0</text>
    </g>
    <g font-size="7" fill="#555" text-anchor="middle">
      <text x="112" y="292">Category 1</text><text x="205" y="292">Category 2</text>
      <text x="298" y="292">Category 3</text><text x="390" y="292">Category 4</text>
    </g>
    <polyline points="112,149.9 205,203.5 298,173.7 390,143.9" fill="none" stroke="var(--bar-blue)" stroke-width="1.2"/>
    <polyline points="112,206.5 205,146.9 298,224.4 390,194.6" fill="none" stroke="var(--line-red)" stroke-width="1.2"/>
    <polyline points="112,218.4 205,218.4 298,188.6 390,129" fill="none" stroke="var(--line-gray)" stroke-width="1.2"/>
    <g fill="var(--bar-blue)">
      <circle cx="112" cy="149.9" r="1.6"/><circle cx="205" cy="203.5" r="1.6"/>
      <circle cx="298" cy="173.7" r="1.6"/><circle cx="390" cy="143.9" r="1.6"/>
    </g>
    <g fill="var(--marker-orange)">
      <rect x="110.4" y="204.9" width="3.2" height="3.2"/><rect x="203.4" y="145.3" width="3.2" height="3.2"/>
      <rect x="296.4" y="222.8" width="3.2" height="3.2"/><rect x="388.4" y="193" width="3.2" height="3.2"/>
    </g>
    <g fill="var(--line-gray)">
      <polygon points="112,216.6 114,220 110,220"/><polygon points="205,216.6 207,220 203,220"/>
      <polygon points="298,186.8 300,190.2 296,190.2"/><polygon points="390,127.2 392,130.6 388,130.6"/>
    </g>
    <g font-size="7.5" fill="#333">
      <line x1="449" x2="465" y1="178" y2="178" stroke="var(--bar-blue)" stroke-width="1.2"/>
      <text x="467" y="181">Series 1</text>
      <line x1="449" x2="465" y1="194" y2="194" stroke="var(--line-red)" stroke-width="1.2"/>
      <text x="467" y="197">Series 2</text>
      <line x1="449" x2="465" y1="209" y2="209" stroke="var(--line-gray)" stroke-width="1.2"/>
      <text x="467" y="212">Series 3</text>
    </g>
  </svg>
  <p class="body-copy" style="top:320px">Lorem ipsum dolor sit amet, <em>consectetur adipiscing elit.</em> Praesent sodales odio sit amet odio tristique quis tempus odio Lorem ipsum dolor sit amet, consectetur adipiscing elit. Lorem ipsum dolor sit amet, consectetur adipiscing elit. Praesent sodales odio sit amet odio tristique quis tempus odio Lorem ipsum dolor sit amet, consectetur adipiscing elit. Lorem ipsum dolor sit amet, consectetur adipiscing elit.</p>
  <footer class="slide-footer" style="top:391px">
    <div class="slide-footer__rule"></div><span class="slide-footer__num">6</span><div class="slide-footer__tail"></div>
  </footer>
</section>

</body>
</html>
```